Supplement Bottle Label Design and Creative Lifestyle Images

We are a medical home consumer brand and we are releasing a supplement line of products called "Velbrook Nutrition". We are in need of a supplement bottle design for our supplement line, Velbrook Nutrition. We are looking for a very appealing, simple, and clean design, but with a medical feel to it.

We would like to see designs with a black background as well as designs with a white background. Bottle size will approximately be 200cc and label will about be 7" x 2.5", but this size is subject to change.

We really like the Pirlen Nutrition design and the Gantry Lab, however, we like the medical style of Nutrition Keystones. Please reference the links below.

To start off, the title of this bottle will be "Calm-Spire". We will need all similar warning about FDA, made in USA, non-GMA, GMP, ect. Please use the formula below to start:

2 Pills per serving
Blueberry pterostilbene - 10mg
Bacopa - 150mg
Gingko Biloba - 50mg
Vinpocetine - 10mg
Alpha-GPC -150mg
TAU - 35mg

https://www.shopvarn.example/Pirlen-Nutrition/b/ref=bl_dp_s_web_48213907562?ie=UTF8&node=48213907562&field-lbr_brands_browse-bin=Pirlen+Nutrition

https://www.shopvarn.example/l/7394208156

https://www.shopvarn.example/Nutrition-Keystones/b/ref=bl_dp_s_web_86420531977?ie=UTF8&node=86420531977&field-lbr_brands_browse-bin=Nutrition+Keystones

Industry/Entity Type

Medical

```html
<!DOCTYPE html>
<html lang="en">
<head>
<meta charset="utf-8">
<title>Velbrook Nutrition – Calm-Spire Label</title>
<link href="https://fonts.googleapis.com/css2?family=Roboto+Condensed:wght@700&family=Open+Sans:ital,wght@1,400&display=swap" rel="stylesheet">
<style>
  :root {
    --page-bg: #ffffff;
    --label-dark: #0d1820;
    --label-mid: #0f3a35;
    --label-green: #0a9257;
    --ink-light: #f2f4f3;
    --ink-soft: #d9e2de;
    --badge-line: #e6e6e6;
  }
  * { margin: 0; padding: 0; box-sizing: border-box; }
  html, body {
    width: 1200px;
    height: 1000px;
    overflow: hidden;
    background: var(--page-bg);
  }
  .canvas {
    position: relative;
    width: 1200px;
    height: 1000px;
  }
  .label {
    position: absolute;
    left: 330px;
    top: 220px;
    width: 560px;
    height: 560px;
    background:
      linear-gradient(90deg, rgba(5,9,12,0.85) 0%, rgba(5,9,12,0) 22%),
      radial-gradient(ellipse 90% 70% at 62% 100%, var(--label-green) 0%, rgba(10,146,87,0) 75%),
      linear-gradient(180deg, var(--label-dark) 0%, var(--label-mid) 55%, #0b6e47 100%);
    overflow: hidden;
  }
  .badge-strip {
    position: absolute;
    left: 0;
    top: 0;
    width: 70px;
    height: 100%;
  }
  .brand {
    position: absolute;
    left: 70px;
    right: 0;
    top: 60px;
    display: flex;
    align-items: center;
    justify-content: center;
    gap: 10px;
  }
  .brand-mark {
    width: 14px;
    height: 14px;
    background: var(--ink-light);
  }
  .brand-name {
    font-family: 'Roboto Condensed', sans-serif;
    font-weight: 700;
    font-size: 30px;
    line-height: 1.05;
    color: var(--ink-light);
    text-align: center;
  }
  .product-title {
    position: absolute;
    left: 70px;
    right: 0;
    top: 242px;
    text-align: center;
    font-family: 'Roboto Condensed', sans-serif;
    font-weight: 700;
    font-size: 52px;
    line-height: 64px;
    letter-spacing: 1px;
    color: var(--ink-light);
    text-transform: uppercase;
  }
  .ingredients {
    position: absolute;
    left: 70px;
    right: 0;
    top: 370px;
    list-style: none;
    text-align: center;
    font-family: 'Open Sans', sans-serif;
    font-style: italic;
    font-size: 16px;
    line-height: 21px;
    color: var(--ink-soft);
  }
</style>
</head>
<body>
<main class="canvas">
  <section class="label" aria-label="Velbrook Nutrition Calm-Spire bottle label">
    <svg class="badge-strip" viewBox="0 0 70 560" aria-label="Certification badges">
      <rect x="14" y="62" width="40" height="40" fill="none" stroke="var(--badge-line)" stroke-width="3"/>
      <circle cx="34" cy="175" r="24" fill="none" stroke="var(--badge-line)" stroke-width="3"/>
      <rect x="14" y="240" width="40" height="56" rx="6" fill="none" stroke="var(--badge-line)" stroke-width="3"/>
      <circle cx="34" cy="375" r="24" fill="none" stroke="var(--badge-line)" stroke-width="3"/>
      <rect x="14" y="440" width="40" height="70" fill="none" stroke="var(--badge-line)" stroke-width="3"/>
    </svg>

    <header class="brand">
      <span class="brand-mark"></span>
      <span class="brand-name">Velbrook<br>Nutrition</span>
    </header>

    <h1 class="product-title">Calm-Spire</h1>

    <ul class="ingredients">
      <li>Blueberry pterostilbene</li>
      <li>Bacopa</li>
      <li>Gingko Biloba</li>
      <li>Vinpocetine</li>
      <li>Alpha-GPC</li>
      <li>TAU</li>
    </ul>
  </section>
</main>
</body>
</html>
```